Wedding invitation

Hello,

I would like the same attached image in a vertical rectangular 3D effect design, same colours,
but without text.

I would like eaxctly like the attachment design, in a long vertical, ration 16:9 size for social media.

```html
<!DOCTYPE html>
<html lang="en">
<head>
<meta charset="utf-8">
<title>Wedding Invitation Frame</title>
<style>
  :root {
    --navy-deep: #00001c;
    --navy-mid: #001a4a;
    --navy-glow: #002a66;
    --steel-shadow: #0a1840;
    --steel-deep: #16306a;
    --steel-dark: #1f3a6a;
    --steel: #3d5d92;
    --steel-mid: #5b7db0;
    --steel-light: #7fa0cc;
    --steel-edge: #3a5280;
    --gold-dark: #a87a1a;
    --gold-deep: #b8861c;
    --gold: #f3c24a;
    --gold-light: #ffe08a;
  }
  html, body {
    margin: 0;
    padding: 0;
    width: 675px;
    height: 1200px;
    overflow: hidden;
    background: var(--navy-deep);
  }
  .invitation {
    position: relative;
    width: 675px;
    height: 1200px;
    background: radial-gradient(ellipse 62% 50% at 50% 50%, var(--navy-glow) 0%, var(--navy-mid) 40%, var(--navy-deep) 100%);
  }
  .frames {
    position: absolute;
    inset: 0;
    width: 675px;
    height: 1200px;
    display: block;
  }
  .frames rect { fill: none; stroke-width: 1; }
</style>
</head>
<body>
  <main class="invitation">
    <svg class="frames" viewBox="0 0 675 1200" xmlns="http://www.w3.org/2000/svg" aria-hidden="true">
      <!-- canvas edge bevel -->
      <g class="edge-bevel">
        <rect x="0.5" y="0.5" width="674" height="1199" style="stroke: var(--steel-edge)"/>
        <rect x="1.5" y="1.5" width="672" height="1197" style="stroke: var(--steel-light)"/>
        <rect x="2.5" y="2.5" width="670" height="1195" style="stroke: var(--steel-mid)"/>
        <rect x="3.5" y="3.5" width="668" height="1193" style="stroke: var(--steel)"/>
        <rect x="4.5" y="4.5" width="666" height="1191" style="stroke: var(--steel-deep)"/>
      </g>
      <!-- gold frame -->
      <g class="gold-frame">
        <rect x="61.5" y="27.5" width="554" height="1144" style="stroke: var(--gold-deep)"/>
        <rect x="62.5" y="28.5" width="552" height="1142" style="stroke: var(--gold)"/>
        <rect x="63.5" y="29.5" width="550" height="1140" style="stroke: var(--gold-light)"/>
        <rect x="64.5" y="30.5" width="548" height="1138" style="stroke: var(--gold)"/>
        <rect x="65.5" y="31.5" width="546" height="1136" style="stroke: var(--gold-dark)"/>
      </g>
      <!-- steel frame -->
      <g class="steel-frame">
        <rect x="29.5" y="57.5" width="618" height="1084" style="stroke: var(--steel-edge)"/>
        <rect x="31" y="59" width="615" height="1081" style="stroke: var(--steel-shadow); stroke-width: 2"/>
        <rect x="32.5" y="60.5" width="612" height="1078" style="stroke: var(--steel-deep)"/>
        <rect x="33.5" y="61.5" width="610" height="1076" style="stroke: var(--steel-dark)"/>
        <rect x="34.5" y="62.5" width="608" height="1074" style="stroke: var(--steel)"/>
        <rect x="35.5" y="63.5" width="606" height="1072" style="stroke: var(--steel-mid)"/>
        <rect x="36.5" y="64.5" width="604" height="1070" style="stroke: var(--steel-light)"/>
        <rect x="37.5" y="65.5" width="602" height="1068" style="stroke: var(--steel-mid)"/>
        <rect x="38.5" y="66.5" width="600" height="1066" style="stroke: var(--steel)"/>
        <rect x="39.5" y="67.5" width="598" height="1064" style="stroke: var(--steel-deep)"/>
      </g>
    </svg>
  </main>
</body>
</html>
```